Brookmere Osteopathy flyer

I want a clean clear DL flyer (but also want an A4 poster) promoting a new Osteopathic business in a semi rural area in Tasmania (Australia).
It can have pictures like the examples attached to show people what Osteopathy is (its like Chiropractic and physiotherapy).
I am the sole practioner and am male, so any pictures would be best to be a white male if possible.
I've attached some wording, you can use all, or none of it
I don't have a phone number for the business yet
info@brookmereosteopathy.example
www.brookmereosteopathy.example
Target Market(s)
Australians, from tradies, professionals, babies to retired people
Industry/Entity Type
Health
Look and feel

```html
<!DOCTYPE html>
<html lang="en">
<head>
<meta charset="utf-8">
<title>Brookmere Osteopathy – DL Flyer</title>
<link href="https://fonts.googleapis.com/css2?family=Poppins:wght@400;500;600;700;800&family=Great+Vibes&display=swap" rel="stylesheet">
<style>
  :root{
    --blue:#1b8fd2;
    --blue-deep:#0a6db3;
    --blue-mid:#0f80c6;
    --orange:#f7922f;
    --orange-soft:#f9a94d;
    --ink:#3a3a3a;
    --ink-soft:#555;
    --rule:#cfd6dc;
    --paper:#ffffff;
    --backdrop:#a3a3a3;
  }
  *{box-sizing:border-box;margin:0;padding:0}
  html,body{width:1134px;height:1200px;overflow:hidden}
  body{background:var(--backdrop);font-family:"Poppins",sans-serif;position:relative}

  .flyer{position:absolute;top:132px;width:443px;height:937px;overflow:hidden;background:var(--paper)}
  .flyer--front{left:101px}
  .flyer--back{left:591px}

  /* ---------- front ---------- */
  .front__band{position:absolute;left:0;right:0;top:502px;bottom:0;
    background:linear-gradient(180deg,var(--blue-mid),var(--blue-deep))}
  .front__art{position:absolute;left:0;top:0;width:443px;height:937px}
  .brand-mark{position:absolute;text-align:center;color:var(--blue);font-weight:600;line-height:1.15}
  .brand-mark--front{left:121px;top:72px;width:200px;font-size:19px}
  .brand-mark__dot{display:inline-block;width:10px;height:10px;border-radius:50%;background:var(--orange);margin-bottom:6px}
  .headline{position:absolute;left:0;width:443px;text-align:center;white-space:nowrap}
  .headline__script{top:160px;left:10px;font-family:"Great Vibes",cursive;color:var(--orange);font-size:62px;line-height:1}
  .headline__feel{top:212px;font-weight:800;font-size:84px;color:var(--ink);line-height:1;letter-spacing:-1px}
  .headline__better{top:280px;left:6px;font-weight:800;font-size:84px;color:var(--blue);line-height:1;letter-spacing:-1px}
  .front__tagline{position:absolute;left:71px;top:697px;color:#fff;font-size:14.5px;line-height:18px}
  .front__tagline strong{display:block;font-weight:700;text-transform:uppercase}
  .front__rule{position:absolute;left:45px;width:352px;top:797px;height:1px;background:rgba(255,255,255,.55)}
  .phone{position:absolute;display:flex;align-items:center;font-weight:700;line-height:1;white-space:nowrap}
  .phone--front{left:45px;top:808px;color:#fff;font-size:39px;gap:8px}
  .phone__icon{flex:none;border-radius:50%;background:var(--orange);display:flex;align-items:center;justify-content:center}
  .url-pill{position:absolute;left:48px;width:347px;height:35px;border-radius:18px;background:var(--orange);
    color:#fff;font-size:13.5px;letter-spacing:1px;white-space:nowrap;
    display:flex;align-items:center;justify-content:center}
  .url-pill b{font-weight:700}
  .url-pill--front{top:862px}
  .url-pill--back{top:859px}

  /* ---------- back ---------- */
  .back__band{position:absolute;left:0;right:0;top:0;height:592px;
    background:linear-gradient(180deg,var(--blue-deep),var(--blue-mid))}
  .reasons{position:absolute;left:44px;top:42px;width:353px;height:443px;background:var(--paper);border-radius:30px;padding:28px 32px 0 32px}
  .reasons__title{font-size:20.5px;font-weight:600;color:var(--ink);line-height:25px}
  .reasons__title span{display:block;color:var(--blue)}
  .reasons__list{list-style:none;margin-top:12px;width:290px}
  .reasons__item{display:flex;align-items:center;gap:6px;height:33px;font-size:13px;color:#222;border-bottom:1px solid var(--rule);white-space:nowrap}
  .reasons__item:last-child{border-bottom:none}
  .reasons__icon{flex:none;width:26px;height:26px;border-radius:50%;display:flex;align-items:center;justify-content:center}
  .reasons__icon--blue{background:var(--blue)}
  .reasons__icon--orange{background:var(--orange)}
  .photo{position:absolute;border-radius:50%;border:5px solid #fff}
  .back__about{position:absolute;left:40px;width:363px;top:653px;text-align:center;font-size:10.6px;line-height:13.3px;color:var(--ink-soft)}
  .back__about b{color:var(--ink);font-weight:600}
  .back__rule{position:absolute;left:44px;width:352px;top:763px;height:1.5px;background:#9aa0a5}
  .brand-mark--back{left:40px;top:792px;width:110px;font-size:13px}
  .phone--back{left:144px;top:777px;color:var(--ink);font-size:21.5px;gap:5px}
  .contact{position:absolute;left:144px;display:flex;align-items:center;gap:8px;font-size:12.5px;font-weight:500;color:var(--ink);white-space:nowrap}
  .contact--email{top:803px}
  .contact--addr{top:826px}
</style>
</head>
<body>

<section class="flyer flyer--front" aria-label="Flyer front">
  <div class="front__band"></div>

  <svg class="front__art" viewBox="0 0 443 937">
    <circle cx="428" cy="20" r="60" fill="none" stroke="var(--blue)" stroke-width="2"/>
    <circle cx="428" cy="20" r="46" fill="var(--blue)"/>
    <g role="img" aria-label="Orange sun decoration">
      <circle cx="0" cy="364" r="62" fill="var(--orange)" opacity=".22"/>
      <circle cx="0" cy="364" r="26" fill="var(--orange)" opacity=".75"/>
    </g>
    <path d="M 376 582 A 162 162 0 1 0 220 685" fill="none" stroke="var(--orange)" stroke-width="28"/>
    <circle cx="220" cy="523" r="128" fill="#fff"/>
    <circle cx="220" cy="523" r="122" fill="url(#mainPhoto)" role="img" aria-label="Photo: osteopath treating a woman's shoulder"/>
    <circle cx="309" cy="685" r="78" fill="#fff"/>
    <circle cx="309" cy="685" r="70" fill="url(#smallPhoto)" role="img" aria-label="Photo: osteopath treating a patient lying face down"/>
    <defs>
      <linearGradient id="mainPhoto" x1="0" y1="0" x2="1" y2="1">
        <stop offset="0" stop-color="#3d8cc7"/>
        <stop offset=".55" stop-color="#d9a083"/>
        <stop offset="1" stop-color="#6f7378"/>
      </linearGradient>
      <linearGradient id="smallPhoto" x1="0" y1="0" x2="1" y2="1">
        <stop offset="0" stop-color="#b8c9d6"/>
        <stop offset="1" stop-color="#3b5c7a"/>
      </linearGradient>
    </defs>
  </svg>

  <div class="brand-mark brand-mark--front"><span class="brand-mark__dot"></span><br>Brookmere<br>Osteopathy</div>

  <div class="headline headline__script">Move better</div>
  <div class="headline headline__feel">FEEL</div>
  <div class="headline headline__better">BETTER</div>

  <p class="front__tagline"><strong>Professional<br>osteopathic care</strong>For pain, tension, and<br>everyday discomfort</p>

  <div class="front__rule"></div>
  <div class="phone phone--front">
    <span class="phone__icon" style="width:34px;height:34px">
      <svg width="20" height="20" viewBox="0 0 24 24"><path d="M6.6 10.8a15.1 15.1 0 0 0 6.6 6.6l2.2-2.2a1 1 0 0 1 1-.25 11.4 11.4 0 0 0 3.6.57 1 1 0 0 1 1 1V20a1 1 0 0 1-1 1A17 17 0 0 1 3 4a1 1 0 0 1 1-1h3.5a1 1 0 0 1 1 1c0 1.25.2 2.450.57 3.57a1 1 0 0 1-.25 1z" fill="#fff"/></svg>
    </span>
    555 0142 0199
  </div>
  <div class="url-pill url-pill--front">www.<b>brookmereosteopathy</b>.example</div>
</section>

<section class="flyer flyer--back" aria-label="Flyer back">
  <div class="back__band"></div>

  <div class="reasons">
    <h2 class="reasons__title">Common reasons people<span>visit an osteopath</span></h2>
    <ul class="reasons__list">
      <li class="reasons__item"><span class="reasons__icon reasons__icon--blue"><svg width="12" height="12" viewBox="0 0 12 12"><path d="M2 6.5l2.5 2.5L10 3" stroke="#fff" stroke-width="2" fill="none"/></svg></span>Back / neck pain</li>
      <li class="reasons__item"><span class="reasons__icon reasons__icon--orange"><svg width="12" height="12" viewBox="0 0 12 12"><path d="M2 6.5l2.5 2.5L10 3" stroke="#fff" stroke-width="2" fill="none"/></svg></span>Headaches / migraines</li>
      <li class="reasons__item"><span class="reasons__icon reasons__icon--blue"><svg width="12" height="12" viewBox="0 0 12 12"><path d="M2 6.5l2.5 2.5L10 3" stroke="#fff" stroke-width="2" fill="none"/></svg></span>Joint and muscle pain</li>
      <li class="reasons__item"><span class="reasons__icon reasons__icon--orange"><svg width="12" height="12" viewBox="0 0 12 12"><path d="M2 6.5l2.5 2.5L10 3" stroke="#fff" stroke-width="2" fill="none"/></svg></span>Pregnancy-related discomfort</li>
      <li class="reasons__item"><span class="reasons__icon reasons__icon--blue"><svg width="12" height="12" viewBox="0 0 12 12"><path d="M2 6.5l2.5 2.5L10 3" stroke="#fff" stroke-width="2" fill="none"/></svg></span>Disc related issues</li>
      <li class="reasons__item"><span class="reasons__icon reasons__icon--orange"><svg width="12" height="12" viewBox="0 0 12 12"><path d="M2 6.5l2.5 2.5L10 3" stroke="#fff" stroke-width="2" fill="none"/></svg></span>Sciatica</li>
      <li class="reasons__item"><span class="reasons__icon reasons__icon--blue"><svg width="12" height="12" viewBox="0 0 12 12"><path d="M2 6.5l2.5 2.5L10 3" stroke="#fff" stroke-width="2" fill="none"/></svg></span>Plantar fasciitis</li>
      <li class="reasons__item"><span class="reasons__icon reasons__icon--orange"><svg width="12" height="12" viewBox="0 0 12 12"><path d="M2 6.5l2.5 2.5L10 3" stroke="#fff" stroke-width="2" fill="none"/></svg></span>Tendonitis / Bursitis</li>
      <li class="reasons__item"><span class="reasons__icon reasons__icon--blue"><svg width="12" height="12" viewBox="0 0 12 12"><path d="M2 6.5l2.5 2.5L10 3" stroke="#fff" stroke-width="2" fill="none"/></svg></span>Adhesive capsulitis (frozen shoulder)</li>
      <li class="reasons__item"><span class="reasons__icon reasons__icon--orange"><svg width="12" height="12" viewBox="0 0 12 12"><path d="M2 6.5l2.5 2.5L10 3" stroke="#fff" stroke-width="2" fill="none"/></svg></span>Tennis / Golfers elbow</li>
    </ul>
  </div>

  <div class="photo" role="img" aria-label="Photo: hands massaging a patient's back" style="left:42px;top:507px;width:126px;height:126px;background:linear-gradient(135deg,#9c6a4f,#e2c0a8)"></div>
  <div class="photo" role="img" aria-label="Photo: osteopath stretching a patient's arm" style="left:153px;top:507px;width:126px;height:126px;background:linear-gradient(135deg,#e7e9ea,#2f8a86)"></div>
  <div class="photo" role="img" aria-label="Photo: osteopath treating a man's shoulder" style="left:269px;top:507px;width:126px;height:126px;background:linear-gradient(135deg,#d8dde1,#a07b66)"></div>

  <p class="back__about">Brookmere Osteopathy use a tailored combination of <b>joint mobilisation/manipulation, stretching, movement, trigger point dry needling and targeted massage to reduce pain and restore optimal function.</b> Hands-on treatment is backed up with rehabilitative exercise prescription and advice. So whether you're recovering from injury or managing chronic discomfort, we're here to help you move better and feel better.</p>

  <div class="back__rule"></div>
  <div class="brand-mark brand-mark--back"><span class="brand-mark__dot"></span><br>Brookmere<br>Osteopathy</div>

  <div class="phone phone--back">
    <span class="phone__icon" style="width:19px;height:19px">
      <svg width="11" height="11" viewBox="0 0 24 24"><path d="M6.6 10.8a15.1 15.1 0 0 0 6.6 6.6l2.2-2.2a1 1 0 0 1 1-.25 11.4 11.4 0 0 0 3.6.57 1 1 0 0 1 1 1V20a1 1 0 0 1-1 1A17 17 0 0 1 3 4a1 1 0 0 1 1-1h3.5a1 1 0 0 1 1 1c0 1.25.2 2.45.57 3.57a1 1 0 0 1-.25 1z" fill="#fff"/></svg>
    </span>
    555 0142 0199
  </div>
  <div class="contact contact--email">
    <span class="phone__icon" style="width:15px;height:15px"><svg width="9" height="9" viewBox="0 0 12 12"><rect x="1" y="2.5" width="10" height="7" fill="none" stroke="#fff" stroke-width="1.4"/><path d="M1 3l5 3.5L11 3" fill="none" stroke="#fff" stroke-width="1.4"/></svg></span>
    info@brookmereosteopathy.example
  </div>
  <div class="contact contact--addr">
    <span class="phone__icon" style="width:15px;height:15px"><svg width="9" height="9" viewBox="0 0 12 12"><path d="M6 11s4-4.2 4-6.5a4 4 0 0 0-8 0C2 6.8 6 11 6 11z" fill="#fff"/><circle cx="6" cy="4.6" r="1.4" fill="var(--orange)"/></svg></span>
    42 Mill Lane, Brookmere
  </div>
  <div class="url-pill url-pill--back">www.<b>brookmereosteopathy</b>.example</div>
</section>

</body>
</html>
```